job report

Designer – Professional Plumbing Job Report Template

Overview

We are seeking a skilled designer to create a professional, easy-to-use Job Report template for a commercial and maintenance plumbing business.
The report will be used for clients, property managers, facilities managers, strata, and retail centres and must clearly communicate findings, works completed, and recommendations in a polished, compliant, and branded format.

The final document must be suitable for PDF delivery, email, and ongoing reuse.

Objectives

Present plumbing works in a clear, professional, and defensible report format

Improve client understanding of findings and recommendations

Provide a repeatable template that can be used across maintenance, reactive, and investigative works

Allow easy insertion of text, tables, and photos

Report Structure (Minimum Inclusions)
1. Cover Page

Company logo and branding

Report title (e.g. Plumbing Job Report / Investigation Report)

Client name

Site address

Job reference / work order number

Date of attendance

Technician / contractor name

2. Client & Site Details

Client / company name

Site address

Contact person

Contact details

Access notes (after-hours, tenant access, etc.)

3. Reason for Attendance

Clear description of why attendance was required

Call-out type (reactive, scheduled maintenance, investigation, emergency, etc.)

Reported issue or scope requested by client

4. Findings / Observations

Detailed findings discovered on site

Condition of pipework, fixtures, drainage, or systems

Any contributing factors identified

Notes on compliance, wear, damage, or risk

(This section should support bullet points and paragraphs.)

5. Works Carried Out

Step-by-step description of works completed

Equipment used (e.g. jetter, CCTV camera, leak detection, flex shaft, etc.)

Repairs, replacements, testing, and verification

Confirmation that systems were tested and operational on completion

6. Photos & Visual Evidence

Clearly labelled photo sections

Before / during / after photos

Space for photo captions and explanations

Logical layout that aligns photos with written findings

7. Recommendations

Clearly separated from works completed

Urgent vs non-urgent recommendations

Preventative maintenance advice

Upgrade or replacement suggestions

Risk-based language where appropriate

8. Limitations & Exclusions

Areas not inspected

Access limitations

Assumptions made during inspection

Items outside scope of works

9. Conclusion

Summary of outcome

Confirmation of current system status

Next steps (if any)

10. Sign-Off

Contractor / technician name

Company name

Date

Optional client acknowledgement section

Design Requirements

Clean, professional layout

Commercial / trade-appropriate styling (not overly creative)

Easy-to-read fonts

Consistent headings and spacing

Logical flow for busy property managers

Editable format (Word / Google Docs / InDesign source file)

Final export-ready PDF version

Bonus (Nice to Have)

Traffic-light system (Green / Amber / Red) for condition reporting

Iconography for findings, repairs, and recommendations

Optional sections for compliance notes (AS/NCC references)

Space for QR codes or job reference numbers

Deliverables

Editable master report template

PDF version

Instructions or notes for ongoing use

```html
<!DOCTYPE html>
<html lang="en">
<head>
<meta charset="utf-8">
<title>Plumbing Job Report – Investigation Report</title>
<link href="https://fonts.googleapis.com/css2?family=Montserrat:wght@700&family=Questrial&display=swap" rel="stylesheet">
<style>
  :root {
    --ink: #1d1d1f;
    --cyan: #55eef6;
    --yellow: #fff200;
    --paper: #f1f2f4;
    --paper-shade: #e4e6ea;
    --brand: #3fd9e6;
  }
  * { box-sizing: border-box; margin: 0; padding: 0; }
  html, body { width: 856px; height: 1200px; overflow: hidden; }
  body { font-family: "Questrial", "Century Gothic", sans-serif; color: var(--ink); }

  .sheet { position: relative; width: 856px; height: 1200px; overflow: hidden; }
  .sheet-texture {
    position: absolute; inset: 0;
    background: linear-gradient(160deg, var(--paper) 0%, #f7f8f9 45%, var(--paper-shade) 100%);
  }

  .brand { position: absolute; left: 52px; top: 38px; display: flex; align-items: center; gap: 12px; }
  .brand-dot { width: 34px; height: 34px; border-radius: 50%; background: var(--yellow); }
  .brand-name {
    font-family: "Montserrat", sans-serif; font-weight: 700; color: var(--brand);
    font-size: 36px; line-height: 1.02; letter-spacing: 1px;
  }

  .report-title {
    position: absolute; right: 52px; top: 46px; text-align: right;
    font-family: "Montserrat", sans-serif; font-weight: 700; font-size: 24px; line-height: 31px;
  }

  .field {
    position: absolute; height: 21px; display: flex; align-items: flex-end;
    font-size: 16.5px; white-space: nowrap;
  }
  .field .fill { flex: 1; border-bottom: 1px solid var(--ink); margin-left: 10px; height: 15px; }
  .rule { position: absolute; height: 0; border-bottom: 1px solid var(--ink); }

  .section-head { position: absolute; left: 52px; width: 752px; height: 22px; }
  .section-head svg { position: absolute; inset: 0; }
  .section-head h2 {
    position: relative; font-family: "Montserrat", sans-serif; font-weight: 700;
    font-size: 15.5px; line-height: 20px; padding-left: 5px;
  }

  .option {
    position: absolute; height: 26px; border: 1.2px solid var(--ink);
    display: flex; align-items: center; justify-content: center; font-size: 16px; white-space: nowrap;
  }

  .photo-label { position: absolute; width: 243px; text-align: center; font-size: 16.5px; }
  .photo-frame { position: absolute; top: 955px; width: 244px; height: 125px; border: 1.2px solid var(--ink); }
</style>
</head>
<body>
<div class="sheet">
  <div class="sheet-texture" role="img" aria-label="Faint light-grey background texture of plumbing tools and fittings"></div>

  <div class="brand">
    <span class="brand-dot"></span>
    <span class="brand-name">TIDEWELL<br>PLUMBING</span>
  </div>

  <div class="report-title">Plumbing Job Report<br>Investigation Report</div>

  <div class="field" style="left:52px;width:392px;top:152px">Client Name:<span class="fill"></span></div>
  <div class="field" style="left:454px;width:350px;top:152px">Date of attendance:<span class="fill"></span></div>
  <div class="field" style="left:52px;width:344px;top:180px">Site address:<span class="fill"></span></div>
  <div class="field" style="left:403px;width:401px;top:180px">Technician / Contractor Name:<span class="fill"></span></div>
  <div class="field" style="left:52px;width:752px;top:208px">Job reference / Work order number:<span class="fill"></span></div>

  <div class="section-head" style="top:244px">
    <svg width="752" height="22" viewBox="0 0 752 22"><rect x="0" y="0" width="180" height="20" fill="var(--cyan)"/><polygon points="170,0 230,0 247,20 183,20" fill="var(--yellow)"/><rect x="0" y="19" width="752" height="2" fill="var(--cyan)"/></svg>
    <h2>Client &amp; Site Details</h2>
  </div>
  <div class="field" style="left:52px;width:392px;top:274px">Client / Company name:<span class="fill"></span></div>
  <div class="field" style="left:454px;width:350px;top:274px">Site address:<span class="fill"></span></div>
  <div class="field" style="left:52px;width:392px;top:302px">Contact person:<span class="fill"></span></div>
  <div class="field" style="left:454px;width:350px;top:302px">Contact details:<span class="fill"></span></div>
  <div class="field" style="left:52px;width:120px;top:330px">Access notes:</div>
  <div class="option" style="left:176px;width:130px;top:329px">After-hours</div>
  <div class="option" style="left:314px;width:130px;top:329px">Tenant access</div>
  <div class="field" style="left:454px;width:350px;top:330px">Other:<span class="fill"></span></div>

  <div class="section-head" style="top:372px">
    <svg width="752" height="22" viewBox="0 0 752 22"><rect x="0" y="0" width="206" height="20" fill="var(--cyan)"/><polygon points="196,0 258,0 275,20 210,20" fill="var(--yellow)"/><rect x="0" y="19" width="752" height="2" fill="var(--cyan)"/></svg>
    <h2>Reason for Attendance</h2>
  </div>
  <div class="field" style="left:52px;width:752px;top:402px">Clear description of why attendance was required:<span class="fill"></span></div>
  <div class="field" style="left:52px;width:140px;top:430px">Call-out type:</div>
  <div class="option" style="left:197px;width:130px;top:429px">Reactive</div>
  <div class="option" style="left:335px;width:193px;top:429px">Scheduled maintenance</div>
  <div class="option" style="left:536px;width:130px;top:429px">Investigation</div>
  <div class="option" style="left:674px;width:130px;top:429px">Emergency</div>
  <div class="field" style="left:52px;width:752px;top:458px">Reported issue or scope requested by client:<span class="fill"></span></div>

  <div class="section-head" style="top:493px">
    <svg width="752" height="22" viewBox="0 0 752 22"><rect x="0" y="0" width="206" height="20" fill="var(--cyan)"/><polygon points="196,0 258,0 275,20 210,20" fill="var(--yellow)"/><rect x="0" y="19" width="752" height="2" fill="var(--cyan)"/></svg>
    <h2>Findings / Observations</h2>
  </div>
  <div class="field" style="left:52px;width:752px;top:523px">• Detailed findings discovered on site:<span class="fill"></span></div>
  <div class="rule" style="left:52px;width:752px;top:568px"></div>
  <div class="field" style="left:52px;width:752px;top:579px">• Condition of pipework, fixtures, drainage, or systems:<span class="fill"></span></div>
  <div class="rule" style="left:52px;width:752px;top:624px"></div>
  <div class="field" style="left:52px;width:752px;top:634px">• Any contributing factors identified:<span class="fill"></span></div>
  <div class="rule" style="left:52px;width:752px;top:680px"></div>
  <div class="field" style="left:52px;width:752px;top:691px">• Notes on compliance, wear, damage, or risk:<span class="fill"></span></div>

  <div class="section-head" style="top:723px">
    <svg width="752" height="22" viewBox="0 0 752 22"><rect x="0" y="0" width="172" height="20" fill="var(--cyan)"/><polygon points="162,0 226,0 243,20 176,20" fill="var(--yellow)"/><rect x="0" y="19" width="752" height="2" fill="var(--cyan)"/></svg>
    <h2>Works Carried Out</h2>
  </div>
  <div class="field" style="left:52px;width:752px;top:754px">Step-by-step description of works completed:<span class="fill"></span></div>
  <div class="rule" style="left:52px;width:752px;top:799px"></div>
  <div class="field" style="left:52px;width:140px;top:810px">Equipment used:</div>
  <div class="option" style="left:197px;width:130px;top:809px">Jetter</div>
  <div class="option" style="left:335px;width:193px;top:809px">CCTV Camera</div>
  <div class="option" style="left:536px;width:130px;top:809px">Leak detection</div>
  <div class="option" style="left:674px;width:130px;top:809px">Flex shaft</div>
  <div class="field" style="left:52px;width:752px;top:838px">Repairs, replacements, testing, and verification:<span class="fill"></span></div>
  <div class="field" style="left:52px;width:752px;top:866px">Confirmation that systems were tested and operational on completion:<span class="fill"></span></div>

  <div class="section-head" style="top:900px">
    <svg width="752" height="22" viewBox="0 0 752 22"><rect x="0" y="0" width="240" height="20" fill="var(--cyan)"/><polygon points="230,0 288,0 305,20 244,20" fill="var(--yellow)"/><rect x="0" y="19" width="752" height="2" fill="var(--cyan)"/></svg>
    <h2>Photos &amp; Visual Evidence</h2>
  </div>
  <div class="photo-label" style="left:52px;top:930px">Before</div>
  <div class="photo-label" style="left:306px;top:930px">During</div>
  <div class="photo-label" style="left:560px;top:930px">After</div>
  <div class="photo-frame" style="left:52px"></div>
  <div class="photo-frame" style="left:306px"></div>
  <div class="photo-frame" style="left:560px"></div>
  <div class="photo-label" style="left:52px;top:1085px">Captions and Explanations</div>
  <div class="photo-label" style="left:306px;top:1085px">Captions and Explanations</div>
  <div class="photo-label" style="left:560px;top:1085px">Captions and Explanations</div>
  <div class="rule" style="left:52px;width:243px;top:1129px"></div>
  <div class="rule" style="left:306px;width:243px;top:1129px"></div>
  <div class="rule" style="left:560px;width:244px;top:1129px"></div>
  <div class="rule" style="left:52px;width:243px;top:1156px"></div>
  <div class="rule" style="left:306px;width:243px;top:1156px"></div>
  <div class="rule" style="left:560px;width:244px;top:1156px"></div>
</div>
</body>
</html>
```